tiling company needs letterhead urgent

We need a logo to represent our company on an electronic letterhead. We are a tiling firm called Corwell Tiling Ltd and undertake all aspects of tiling work. The final design of the logo should incorporate the type of work we do and should be modern. We do not want any designs which may be considered 'novelty' or 'cartoonish.' No characters please, we require something sleek and contemporary . Please ensure the company name is central to your design ,Corwell Tiling Ltd

Industry/Entity Type

Electronic

Requirements
Must have
• text on letterhead to included

Registered address 41 Birch lane Failsworth Manchester M359QT
Company number 5267093
VAT no 412957386
Mobile no 07831659047
Office no 0161 574 8192
Web :www.floorvane.co.uk
Email : gareth@floorvane.co.uk
Nice to have
• a tile theme

```html
<!DOCTYPE html>
<html lang="en">
<head>
<meta charset="utf-8">
<title>Corwell Tiling Ltd – Letterhead</title>
<link rel="stylesheet" href="https://fonts.googleapis.com/css2?family=Nunito+Sans:wght@300;700&display=swap">
<style>
  :root {
    --paper: #fdfdfd;
    --ink: #333333;
    --tile-umber: #6f5a46;
    --tile-sand: #a58e72;
    --tile-orange: #f58a35;
    --tile-lime: #a6cd48;
    --tile-aqua: #5bc6cf;
    --tile-violet: #7e5ea7;
    --tile-coral: #ef6279;
    --tile-blush: #f5add0;
    --tile-silver: #d1d3d4;
  }
  * { margin: 0; padding: 0; box-sizing: border-box; }
  html, body { width: 849px; height: 1200px; overflow: hidden; background: var(--paper); }
  .letterhead { position: relative; width: 849px; height: 1200px; background: var(--paper); font-family: "Nunito Sans", sans-serif; color: var(--ink); }
  .tile-strip { position: absolute; top: 33px; left: 0; width: 849px; height: 72px; }
  .tile { position: absolute; top: 0; height: 72px; width: 72px; }
  .tile--edge { width: 60px; }
  .brand { position: absolute; top: 140px; left: 0; width: 849px; text-align: center; font-weight: 700; font-size: 54px; line-height: 72px; letter-spacing: 0.5px; color: var(--ink); }
  .contact { position: absolute; top: 225px; left: 0; width: 849px; text-align: center; font-weight: 300; font-size: 15px; line-height: 19px; font-style: normal; }
</style>
</head>
<body>
<main class="letterhead">
  <div class="tile-strip">
    <div class="tile tile--edge" style="left:15px;background:var(--tile-umber)"></div>
    <div class="tile" role="img" aria-label="Ornamental patterned tile in sand" style="left:99px;background:var(--tile-sand)"></div>
    <div class="tile" style="left:195px;background:var(--tile-orange)"></div>
    <div class="tile" role="img" aria-label="Ornamental patterned tile in lime green" style="left:291px;background:var(--tile-lime)"></div>
    <div class="tile" style="left:387px;background:var(--tile-aqua)"></div>
    <div class="tile" role="img" aria-label="Ornamental patterned tile in violet" style="left:484px;background:var(--tile-violet)"></div>
    <div class="tile" style="left:580px;background:var(--tile-coral)"></div>
    <div class="tile" role="img" aria-label="Ornamental patterned tile in blush pink" style="left:676px;background:var(--tile-blush)"></div>
    <div class="tile tile--edge" style="left:772px;background:var(--tile-silver)"></div>
  </div>

  <h1 class="brand">Corwell Tiling Ltd</h1>

  <address class="contact">
    Address:&nbsp; 41 Birch lane Failsworth Manchester M359QT<br>
    Company number:&nbsp; 5267093<br>
    VAT no:&nbsp; 412957386<br>
    Mobile no:&nbsp;&nbsp; 07831659047<br>
    Office no:&nbsp; 0161 574 8192<br>
    Web:&nbsp; www.floorvane.co.uk<br>
    Email:&nbsp; gareth@floorvane.co.uk
  </address>
</main>
</body>
</html>
```